Flyer-Design für Open Workspace Lösung
Zielgruppe
Was machen wir? Open Workspace Lösung für Ärzte und Psychotherapeuten.
Zielgruppe: Unser Angebot richtet sich an Ärzte, Psychologen, Psychotherapeuten, Heilpraktiker für Psychotherapie (HeilprG) sowie Coaches und Supervisoren mit vergleichbarem und zertifiziertem Hintergrund. Darüber hinaus stehen die Räume auch für Seminare, Workshops oder Gruppenangebote zur Verfügung.
Aufgabenstellung
1. Die Word-Skizze ist ein Entwurf, der gerne verändert werden kann.
2. Das Foto in der oberen Hälfte ist ein Platzhalter. Es ist zwar real aber wir haben leider noch kein gutes Foto der fertigen Räume. Daher sollte, falls ein Bild verwendet wird, eine bearbeitbare Version mitgeliefert werden, damit wir das Bild noch austauschen können. Es muss kein Bild im Flyer verwendet werden, kann aber.
3. Unser Logo sollte auf den Flyer kommen. Es gibt das Logo mit und ohne Text. Beide hängen wir als Datei mit an.
4. Wir haben eine Website: www.praxis-sonnenwiese.de
Der Flyer sollte zu dieser passen. Die Schriftart der Website ist font-famliy: 'Lato', sans-serif und sollte verwendet werden.
5. Die Farbe (türkis) ist vorgegeben. Die Definition ist: #0CE0AE
Die Grautöne der Website sind folgende: #444444, #555444, #5A5A5A, #888888, #CCCCCC #F4F4F4
6. wir hätten gerne einen one-pager, den man als Werbung an Emails anhängen und im Internet veröffentlichen kann und einen Flyer, der ausgedruckt ausliegen kann

```html
<!DOCTYPE html>
<html lang="de">
<head>
<meta charset="utf-8">
<title>Praxis an der Sonnenwiese – Flyer</title>
<link href="https://fonts.googleapis.com/css2?family=Lato:wght@300;400;700&display=swap" rel="stylesheet">
<style>
  :root {
    --teal: #0CE0AE;
    --teal-dark: #0aa982;
    --olive-grey: #555444;
    --mid-grey: #888888;
    --text-dark: #444444;
    --line-grey: #CCCCCC;
    --paper: #ffffff;
    --backdrop: #7a7c7c;
  }
  * { box-sizing: border-box; margin: 0; padding: 0; }
  html, body { width: 1200px; height: 3180px; overflow: hidden; }
  body { background: var(--backdrop); font-family: 'Lato', sans-serif; color: var(--text-dark); }

  .flyer {
    position: absolute; left: 45px; top: 807px;
    width: 1110px; height: 1566px; background: var(--paper);
    box-shadow: 0 6px 18px rgba(0,0,0,.35); overflow: hidden;
  }
  .block { position: absolute; }

  .brand-box { left: 0; top: 0; width: 416px; height: 144px; background: var(--paper);
    display: flex; align-items: center; gap: 22px; padding-left: 34px; }
  .brand-square { width: 46px; height: 46px; background: var(--teal-dark); flex: none; }
  .brand-name { font-weight: 300; font-size: 27px; line-height: 1.05; letter-spacing: 2px; color: var(--mid-grey); text-transform: uppercase; }

  .hero-photo { left: 416px; top: 0; width: 694px; height: 516px;
    background: linear-gradient(135deg, #e9e6df 0%, #cfc7b8 40%, #8d8574 70%, #5e5a4c 100%); }
  .hero-panel { left: 0; top: 144px; width: 416px; height: 372px; background: var(--olive-grey); }
  .hero-tint { left: 416px; top: 144px; width: 346px; height: 372px; background: var(--teal); opacity: .82; }

  .hero-text { left: 68px; top: 196px; width: 900px; color: #fff; }
  .hero-title { font-weight: 700; font-size: 56px; line-height: 1.1; }
  .hero-sub { font-weight: 400; font-size: 31px; margin-top: 6px; }
  .hero-copy { font-size: 17.5px; line-height: 1.3; margin-top: 26px; width: 700px; }
  .hero-copy + .hero-copy { margin-top: 22px; }

  .room-photo { left: 0; top: 516px; width: 416px; height: 718px;
    background: linear-gradient(180deg, #eeeae2 0%, #dcd6cb 45%, #b7a48a 70%, #8a5a34 100%); }

  .info-panel { left: 416px; top: 516px; width: 694px; height: 516px; background: var(--teal);
    padding: 34px 58px 0 58px; color: var(--text-dark); }
  .section-head { display: flex; align-items: center; gap: 14px; font-size: 21px; font-weight: 400; color: #333; }
  .section-head::after { content: ""; width: 110px; height: 2px; background: #333; }
  .info-copy { font-size: 16.5px; line-height: 1.36; text-align: justify; margin-top: 14px; margin-bottom: 36px; }
  .price-list { list-style: none; margin-top: 14px; font-size: 16.5px; line-height: 1.36; }
  .price-list li { position: relative; padding-left: 30px; }
  .price-list li::before { content: "•"; position: absolute; left: 4px; }

  .audience-panel { left: 416px; top: 1032px; width: 694px; height: 202px; background: var(--mid-grey);
    padding: 22px 58px 0 58px; color: #fff; }
  .audience-title { font-size: 26px; font-weight: 700; }
  .audience-copy { font-size: 16.5px; line-height: 1.36; text-align: justify; margin-top: 10px; }

  .contact-area { left: 68px; top: 1268px; width: 760px; font-size: 17.5px; line-height: 1.35; color: var(--text-dark); }
  .contact-area a { color: var(--teal-dark); text-decoration: none; }
  .contact-area p + p { margin-top: 22px; }
  .people { display: flex; margin-top: 32px; }
  .person { width: 430px; }
  .person-name { font-size: 21px; font-weight: 400; color: #222; margin-bottom: 6px; }
  .contact-line { display: flex; align-items: center; gap: 14px; font-size: 17px; margin-top: 4px; }
  .contact-line svg { width: 16px; height: 16px; flex: none; }

  .footer-brand { left: 874px; top: 1270px; width: 200px; }
  .footer-square { width: 90px; height: 90px; background: var(--teal-dark); margin-bottom: 26px; }
  .footer-name { font-weight: 300; font-size: 25px; line-height: 1.05; letter-spacing: 3px; color: var(--mid-grey); text-transform: uppercase; }

  .bar-teal { left: 0; top: 1540px; width: 554px; height: 26px; background: var(--teal); }
  .bar-grey { left: 554px; top: 1540px; width: 556px; height: 26px; background: var(--olive-grey); }
</style>
</head>
<body>
  <main class="flyer">
    <div class="block hero-photo" role="img" aria-label="Foto eines hellen Therapieraums mit Sessel, Stehlampe, Kommode und Zimmerpflanze"></div>
    <div class="block hero-panel"></div>
    <div class="block hero-tint"></div>

    <div class="block brand-box">
      <span class="brand-square"></span>
      <span class="brand-name">Praxis an der<br>Sonnenwiese</span>
    </div>

    <div class="block hero-text">
      <h1 class="hero-title">Praxis an der Sonnenwiese</h1>
      <p class="hero-sub">Flexible Raummiete im Herzen von München</p>
      <p class="hero-copy">Sie suchen schöne und hochwertig ausgestattete Räume in zentraler Lage für Therapie, Coaching oder Seminare? Sie möchten zeitlich flexibel arbeiten und Ihre monatlichen Fixkosten niedrig halten?</p>
      <p class="hero-copy">Unsere Praxis an der Sonnenwiese bietet Ihnen genau das.</p>
    </div>

    <div class="block room-photo" role="img" aria-label="Foto eines Seminarraums mit schwarzen Stühlen, Teppich, Parkettboden und Balkontür"></div>

    <section class="block info-panel">
      <h2 class="section-head">Die Praxis</h2>
      <p class="info-copy">Die Praxis liegt direkt am Stadtpark, ist sehr ruhig und bietet einen wunderschönen Blick ins Grüne. In ihr stehen fünf frisch renovierte und hochwertig ausgestattete Therapieräume sowie zwei Seminarräume zur Verfügung. An welchem Tag, zu welcher Uhrzeit und für wie viele Stunden Sie diese mieten, können Sie entscheiden, ganz so wie es Ihr Bedarf von Woche zu Woche oder auch für das ganze Jahr verlangt.</p>
      <h2 class="section-head">Die Preise</h2>
      <ul class="price-list">
        <li>Verschiedene Preismodelle bieten Ihnen je nach Bedarf volle Flexibilität. Sie können Räume entweder für einzelne Stunden oder im Abonnement mieten.</li>
        <li>Bei der Miete von einzelnen Stunden fallen keinerlei laufende Kosten an.</li>
        <li>Über ein Abonnement bieten wir Ihnen sehr attraktive Preise ab einer Stunde pro Woche.</li>
        <li>Sie können dadurch selbst bestimmen ob und in welcher Höhe Ihnen monatliche Fixkosten entstehen und welches Modell für Sie am besten geeignet ist.</li>
      </ul>
    </section>

    <section class="block audience-panel">
      <h2 class="audience-title">An wen richtet sich unser Angebot?</h2>
      <p class="audience-copy">Unser Angebot richtet sich an Ärzte, Psychologen, Psychotherapeuten, Heilpraktiker für Psychotherapie (HeilprG) sowie Coaches und Supervisoren mit vergleichbarem und zertifiziertem Hintergrund. Darüber hinaus stehen die Räume auch für Seminare, Workshops oder Gruppenangebote zur Verfügung.</p>
    </section>

    <section class="block contact-area">
      <p>Die genauen Konditionen, Bilder und alle weiteren Informationen finden Sie auf der Website: <a href="#">www.praxis-sonnenwiese.de</a></p>
      <p>Bei Fragen, für weitere Informationen oder zur Vereinbarung einer Besichtigung - gerne auch virtuell über Video - kontaktieren Sie uns:</p>
      <div class="people">
        <div class="person">
          <div class="person-name">Lena Hofbauer-Krenn</div>
          <div class="contact-line"><svg viewBox="0 0 16 16"><rect width="16" height="16" rx="2" fill="#444"/><path d="M3 5h10v6H3z M3 5l5 4 5-4" fill="none" stroke="#fff" stroke-width="1.2"/></svg>kontakt@praxis-sonnenwiese.de</div>
          <div class="contact-line"><svg viewBox="0 0 16 16"><rect width="16" height="16" rx="2" fill="#444"/><path d="M5 3.5l2 2-1 1.5c.6 1.3 1.7 2.4 3 3l1.5-1 2 2-1.3 1.5C7.5 12 4 8.5 3.5 4.8z" fill="#fff"/></svg>0176 55501234</div>
        </div>
        <div class="person">
          <div class="person-name">Markus Krenn</div>
          <div class="contact-line"><svg viewBox="0 0 16 16"><rect width="16" height="16" rx="2" fill="#444"/><path d="M3 5h10v6H3z M3 5l5 4 5-4" fill="none" stroke="#fff" stroke-width="1.2"/></svg>kontakt@praxis-sonnenwiese.de</div>
          <div class="contact-line"><svg viewBox="0 0 16 16"><rect width="16" height="16" rx="2" fill="#444"/><path d="M5 3.5l2 2-1 1.5c.6 1.3 1.7 2.4 3 3l1.5-1 2 2-1.3 1.5C7.5 12 4 8.5 3.5 4.8z" fill="#fff"/></svg>0177 55509876</div>
        </div>
      </div>
    </section>

    <div class="block footer-brand">
      <div class="footer-square"></div>
      <div class="footer-name">Praxis an<br>der Sonnen-<br>wiese</div>
    </div>

    <div class="block bar-teal"></div>
    <div class="block bar-grey"></div>
  </main>
</body>
</html>
```